Briar Crest personal care products line

I need a label design for a line of shampoo, conditioner, beard oil, body butter, massage oil, all containing Hemp oil, All Natural product. No phosphates,
I want the design to feel unisex but want to keep it clean as possible. This is for upscale salons and needs to say on the label professional styling products on the label. Please visit my facebook page www.plumvale.net/briarcrest to see the description of the product benefits. I am attaching some ideas I like as well as the briar crest logo. I would like to see any color of bottle you best think will suit this product as well as new logo design. I am not set on any of these elements. Just the name Briar Crest.
Updates

Project Deadline Extended Reason: I have extended the deadline as I had not filled out the description for the design as it should be. I have also added some features that will define the idea as to what we need. I am open to any desing using Briar Crest. The tag line is not anything I am determined to keep either. Please just be creative and help come up with a great product label for this name and product.Thank you to all ! Added Tuesday, June 2, 2015

Target Market(s)

Salons and upper end market

Industry/Entity Type

Cosmetology

Font styles to use
Serif
Sans Serif

Requirements
Must have
• Logo
Nice to have
• Bottle and packaging ideas on color and shape of bottle

```html
<!DOCTYPE html>
<html lang="en">
<head>
<meta charset="utf-8">
<title>Briar Crest – Label Concept</title>
<link rel="stylesheet" href="https://fonts.googleapis.com/css2?family=Bodoni+Moda:wght@500&family=Arimo:wght@400&family=Libre+Baskerville:wght@400;700&display=swap">
<style>
  :root {
    --bg-top: #2e2e2e;
    --bg-bottom: #0a0a0a;
    --label: #4e4f43;
    --ink: #262622;
    --banner: #809a38;
    --banner-edge: #141414;
    --banner-text: #cfe29a;
    --accent: #93ad4c;
    --band: #879c3b;
    --band-art: #9bb04f;
    --art: #a9c46a;
  }
  html, body {
    margin: 0;
    padding: 0;
    width: 1200px;
    height: 1000px;
    overflow: hidden;
    background: var(--bg-bottom);
  }
  .board {
    display: block;
    width: 1200px;
    height: 1000px;
  }
  .wordmark {
    font-family: "Bodoni Moda", "Didot", serif;
    font-weight: 500;
    fill: var(--ink);
  }
  .tagline {
    font-family: "Arimo", Arial, sans-serif;
    fill: var(--ink);
  }
  .banner-small {
    font-family: "Libre Baskerville", Georgia, serif;
    font-size: 11px;
    fill: var(--banner-text);
    letter-spacing: 0.5px;
  }
  .banner-main {
    font-family: "Libre Baskerville", Georgia, serif;
    font-weight: 700;
    font-size: 20px;
    fill: var(--ink);
  }
  .site-url {
    font-family: "Arimo", Arial, sans-serif;
    font-size: 30px;
    fill: var(--accent);
  }
</style>
</head>
<body>
<svg class="board" viewBox="0 0 1200 1000" xmlns="http://www.w3.org/2000/svg">
  <defs>
    <linearGradient id="backdrop" x1="0" y1="0" x2="0" y2="1">
      <stop offset="0" stop-color="var(--bg-top)"/>
      <stop offset="1" stop-color="var(--bg-bottom)"/>
    </linearGradient>
  </defs>

  <rect class="backdrop" x="0" y="0" width="1200" height="793" fill="url(#backdrop)"/>

  <!-- Front label -->
  <g class="label-front">
    <ellipse cx="360" cy="220" rx="305" ry="165" fill="var(--label)"/>
    <text class="wordmark" x="140" y="212" font-size="60" textLength="220" lengthAdjust="spacingAndGlyphs">BRIAR</text>
    <text class="wordmark" x="140" y="266" font-size="60" textLength="220" lengthAdjust="spacingAndGlyphs">CREST</text>
    <text class="tagline" x="135" y="285" font-size="13.5" textLength="230" lengthAdjust="spacingAndGlyphs">PROFESSIONAL  STYLING PRODUCTS</text>
    <rect class="illustration-area" x="395" y="112" width="170" height="250" rx="20" fill="var(--art)" opacity="0.35" role="img" aria-label="Line illustration of a head in profile with hair in a low bun and a hemp leaf"/>

    <!-- Product banners: flat placeholder strips in place of the leaf artwork -->
    <g class="banners" role="img" aria-label="Three green hemp-leaf shaped banners carrying the product claims">
      <g class="banner banner-claims-bottom" transform="translate(255 420) rotate(25)">
        <rect x="-112" y="-12" width="224" height="24" rx="12" fill="var(--banner-edge)"/>
        <rect x="-108" y="-10" width="216" height="20" rx="10" fill="var(--banner)"/>
        <text class="banner-small" x="0" y="4" text-anchor="middle">NO PHOSPHATES</text>
      </g>
      <g class="banner banner-claims-top" transform="translate(300 324) rotate(-4)">
        <rect x="-142" y="-13" width="284" height="26" rx="13" fill="var(--banner-edge)"/>
        <rect x="-138" y="-11" width="276" height="22" rx="11" fill="var(--banner)"/>
        <text class="banner-small" x="0" y="4" text-anchor="middle">ALL NATURAL</text>
      </g>
      <g class="banner banner-product" transform="translate(300 374) rotate(7)">
        <rect x="-168" y="-19" width="336" height="38" rx="19" fill="var(--banner-edge)"/>
        <rect x="-164" y="-16" width="328" height="32" rx="16" fill="var(--banner)"/>
        <text class="banner-main" x="0" y="7" text-anchor="middle" textLength="190" lengthAdjust="spacingAndGlyphs">BODY BUTTER</text>
      </g>
    </g>
  </g>

  <!-- Back label -->
  <g class="label-back">
    <ellipse cx="832" cy="522" rx="306" ry="160" fill="var(--label)"/>
    <text class="wordmark" x="610" y="510" font-size="58" textLength="215" lengthAdjust="spacingAndGlyphs">BRIAR</text>
    <text class="wordmark" x="610" y="566" font-size="58" textLength="215" lengthAdjust="spacingAndGlyphs">CREST</text>
    <text class="site-url" x="833" y="626" text-anchor="middle">briarcrestco.com</text>
  </g>

  <!-- Brand band -->
  <g class="brand-band">
    <rect x="0" y="793" width="1200" height="207" fill="var(--band)"/>
    <text class="wordmark" x="45" y="878" font-size="80" textLength="305" lengthAdjust="spacingAndGlyphs">BRIAR</text>
    <text class="wordmark" x="45" y="954" font-size="80" textLength="300" lengthAdjust="spacingAndGlyphs">CREST</text>
    <text class="tagline" x="45" y="976" font-size="18" textLength="307" lengthAdjust="spacingAndGlyphs">PROFESSIONAL  STYLING PRODUCTS</text>
    <rect class="band-illustration" x="765" y="793" width="380" height="207" fill="var(--band-art)" opacity="0.6" role="img" aria-label="Enlarged line drawing of the hair bun with a hemp leaf, in light green"/>
  </g>
</svg>
</body>
</html>
```